Letterhead for Midwest Law Firm

Our law firm does estate planning and trust administration in Wisconsin and Illinois. We recently obtained a new logo and need to incorporate it into new stationary. The stationary needs to list out the attorneys at the firm, but we will want 3 variations, one with three attorneys, one with six, and one with six plus the names of states where each is licensed to practice (possibly as an asterisk with notation somewhere towards bottom of page. As with most traditional law practices, letterhead should be conservative and convey predictability and reliability. We view our brand as being primarily reliability, with prestige as a secondary element. We are upmarket, but would like to avoid seeming pretentious or "slick". We are a smaller firm with a personal touch.

Target Market(s)

Affluent Midwestern Americans approaching at or approaching retirement age.

Industry/Entity Type

Legal

Font styles to use
Serif
Sans Serif

Requirements
Must have
• Must use our logo. Must comply with Brennick Legal Guild Ethics rules: https://www.halvorjudic.org/courts/offices/docs/pqmtnv20annotated.pdf. Must be conventional. Must list names of attorneys and provide contact information for firm. Note that we are asking for three designs with very minor variations. Also, designer must provide letterhead in a format that is industry-standard for stationary printers.
Nice to have
• We would appreciate an alternate version that will look reasonable when printed on a black-and-white printer. Designer can use judgment as to whether to have use grayscale, black/white, or something in between.
Should not have
• No "motto" or "visit our website" extraneous materials. putting the website address somewhere is fine, but overall there is a lot of required text, and we'd like to not appear cluttered.

```html
<!DOCTYPE html>
<html lang="en">
<head>
<meta charset="utf-8">
<title>Halloway &amp; Brandt LLP — Letterhead</title>
<link rel="stylesheet" href="https://fonts.googleapis.com/css2?family=Libre+Baskerville:wght@700&family=Tinos&display=swap">
<style>
  :root {
    --backdrop: #e4e4e4;
    --paper: #ffffff;
    --navy: #2b2840;
    --gold: #f2a71b;
    --sky: #2aa3e0;
    --ink: #33314a;
    --faint: #f3f3f5;
  }
  * { margin: 0; padding: 0; box-sizing: border-box; }
  html, body {
    width: 1200px; height: 1200px; overflow: hidden;
    background: var(--backdrop);
  }
  .letterhead {
    position: absolute; left: 136px; top: 0;
    width: 928px; height: 1200px;
    background: var(--paper);
    font-family: "Tinos", "Times New Roman", serif;
    color: var(--ink);
  }
  .brand {
    position: absolute; left: 38px; top: 42px;
    display: flex; align-items: center; gap: 14px;
  }
  .brand-dot {
    width: 30px; height: 30px; border-radius: 50%;
    background: var(--gold);
  }
  .brand-name {
    font-family: "Libre Baskerville", "Times New Roman", serif;
    font-weight: 700; font-size: 26px; color: var(--navy);
    letter-spacing: 0.2px;
  }
  .roster {
    position: absolute; left: 650px; top: 30px;
    list-style: none; font-size: 14.5px; line-height: 18px;
    color: var(--ink);
  }
  .backdrop-mark {
    position: absolute; left: 264px; top: 395px;
    width: 400px; height: 400px; border-radius: 50%;
    background: var(--faint);
  }
  .contact-bar {
    position: absolute; left: 38px; right: 30px; top: 1138px;
    display: flex; justify-content: space-between; align-items: center;
    font-size: 13.5px; color: var(--ink);
  }
  .contact-item { display: flex; align-items: center; gap: 8px; }
  .contact-item svg { width: 24px; height: 26px; fill: var(--gold); }
  .rule-sky {
    position: absolute; left: 0; right: 0; top: 1174px; height: 4px;
    background: var(--sky);
  }
  .band-navy {
    position: absolute; left: 0; right: 0; top: 1178px; height: 22px;
    background: var(--navy);
  }
</style>
</head>
<body>
  <main class="letterhead">
    <header class="brand">
      <span class="brand-dot"></span>
      <span class="brand-name">Halloway &amp; Brandt LLP</span>
    </header>

    <ul class="roster">
      <li>MARTIN L. HALLOWAY, Attorney</li>
      <li>THOMAS E. HALLOWAY, Attorney</li>
      <li>CARLA J. WENDT, Paralegal</li>
    </ul>

    <div class="backdrop-mark" aria-hidden="true"></div>

    <footer class="contact-bar">
      <span class="contact-item">
        <svg viewBox="0 0 24 26" aria-hidden="true"><path d="M12 1a8 8 0 0 0-8 8c0 6 8 14 8 14s8-8 8-14a8 8 0 0 0-8-8zm0 11a3 3 0 1 1 0-6 3 3 0 0 1 0 6z"/><ellipse cx="12" cy="24.5" rx="5" ry="1.3"/></svg>
        218 E. Calder Avenue, Suite 300
      </span>
      <span class="contact-item">
        <svg viewBox="0 0 24 26" aria-hidden="true"><path d="M12 1a8 8 0 0 0-8 8c0 6 8 14 8 14s8-8 8-14a8 8 0 0 0-8-8zm0 11a3 3 0 1 1 0-6 3 3 0 0 1 0 6z"/><ellipse cx="12" cy="24.5" rx="5" ry="1.3"/></svg>
        Lakeford, WI&nbsp; 53990
      </span>
      <span class="contact-item">
        <svg viewBox="0 0 24 26" aria-hidden="true"><path d="M6 2l4 0 2 6-3 2c1 3 3 6 6 8l2-3 6 2 0 4c0 1-1 2-2 2C11 23 3 14 3 4c0-1 1-2 3-2z"/></svg>
        555-201-4400
      </span>
      <span class="contact-item">
        <svg viewBox="0 0 24 26" aria-hidden="true"><path d="M7 2h9l3 3v5h2a2 2 0 0 1 2 2v11a2 2 0 0 1-2 2H3a2 2 0 0 1-2-2V12a2 2 0 0 1 2-2h4zm2 2v6h8V6h-2V4zM12 14v2h2v-2zm4 0v2h2v-2zm-4 4v2h2v-2zm4 0v2h2v-2zM4 12v10h4V12z"/></svg>
        555-201-4410
      </span>
    </footer>

    <div class="rule-sky"></div>
    <div class="band-navy"></div>
  </main>
</body>
</html>
```